Simple, Professional and neat business card design for Vendralo Inc.

We're looking to re-vamp our business card design. We're a supplier of innovative feed ingredients for the North American animal agriculture industry. We are located in Lucknow, Ontario, Canada and our flagship product is a product that prevents milk fever in dairy cows when the calve, it is fed before calving and is very effective compared to other alternatives available on the market today.

Our company has Danish roots and we import all of our product from our Danish partner/manufacturer in Denmark. We like our design to embrace high professionalism while remaining neat and simple.

Target Market(s)

B2B, Feed Mills, Veterinary Clinics, Large integrators/producers,

Industry/Entity Type

Agribusiness

Contact Information for Business Card

We like the rounded corners because they make the card easy to sit in a wallet and not many use it so it makes the card stand out, just possibly something to take account for during the design.

As you can also see on the sliders below, looking for a that simple but proffesional scandinavian design.

Requirements
Nice to have
• Rounded corners
Should not have
• Too vibrant

```html
<!DOCTYPE html>
<html lang="en">
<head>
<meta charset="UTF-8">
<title>Vendralo Inc. – Business Card</title>
<link rel="stylesheet" href="https://fonts.googleapis.com/css2?family=Nunito:wght@400;800;900&display=swap">
<style>
  :root {
    --brand-blue: #1e5ca6;
    --navy: #0e2f52;
    --bar-blue: #4d88c9;
    --white: #ffffff;
    --edge: #c9d3e0;
    --page: #ffffff;
  }
  * { box-sizing: border-box; margin: 0; padding: 0; }
  html, body {
    width: 1200px; height: 720px; overflow: hidden;
    background: var(--page);
    font-family: "Nunito", sans-serif;
  }
  .card {
    position: relative;
    width: 1200px; height: 720px;
    background: var(--white);
    border: 2px solid var(--edge);
    border-radius: 44px;
    overflow: hidden;
  }
  .brand {
    position: absolute; top: 136px; left: 320px;
    display: flex; align-items: center; gap: 26px;
  }
  .brand-mark {
    width: 90px; height: 90px;
    background: var(--brand-blue);
    border-radius: 12px;
  }
  .brand-name {
    font-weight: 900; font-size: 54px; letter-spacing: 0.5px;
    color: var(--brand-blue); text-transform: uppercase;
  }
  .divider {
    position: absolute; top: 330px; left: 0; width: 100%; height: 17px;
    background: var(--brand-blue);
  }
  .person-name {
    position: absolute; left: 78px; top: 446px;
    font-weight: 800; font-size: 52px; color: var(--brand-blue);
  }
  .contact-panel {
    position: absolute; top: 347px; left: 671px; right: 0; height: 271px;
    background: var(--navy);
    padding: 6px 14px 0 15px;
    display: flex; flex-direction: column; gap: 12px;
  }
  .contact-row { display: flex; height: 58px; gap: 14px; }
  .contact-icon {
    width: 56px; flex: none;
    display: flex; align-items: center; justify-content: center;
  }
  .contact-icon svg { width: 34px; height: 34px; }
  .contact-value {
    flex: 1; background: var(--bar-blue);
    color: var(--white); font-size: 32px; font-weight: 400;
    display: flex; align-items: center; padding-left: 32px;
  }
  .address-band {
    position: absolute; left: 0; right: 0; bottom: 0; height: 102px;
    background: var(--navy); color: var(--white);
    font-size: 34px; font-weight: 400;
    display: flex; justify-content: center; padding-top: 4px;
  }
</style>
</head>
<body>
<div class="card">
  <div class="brand">
    <div class="brand-mark"></div>
    <div class="brand-name">Vendralo Inc.</div>
  </div>

  <div class="divider"></div>

  <div class="person-name">Henrik Mortensen</div>

  <div class="contact-panel">
    <div class="contact-row">
      <div class="contact-icon">
        <svg viewBox="0 0 34 34" aria-hidden="true"><rect x="3" y="8" width="28" height="19" fill="#fff"/><path d="M3 8 L17 19 L31 8" fill="none" stroke="#0e2f52" stroke-width="2.5"/></svg>
      </div>
      <div class="contact-value">henrik@vendralo.com</div>
    </div>
    <div class="contact-row">
      <div class="contact-icon">
        <svg viewBox="0 0 34 34" aria-hidden="true" fill="none" stroke="#fff" stroke-width="2.5"><circle cx="17" cy="17" r="13"/><ellipse cx="17" cy="17" rx="6" ry="13"/><path d="M4 17 H30 M6 10 H28 M6 24 H28"/></svg>
      </div>
      <div class="contact-value">www.vendralo.com</div>
    </div>
    <div class="contact-row">
      <div class="contact-icon">
        <svg viewBox="0 0 34 34" aria-hidden="true" fill="#fff"><path d="M3 12 C3 6 31 6 31 12 L31 15 L24 15 L23 11 C19 10 15 10 11 11 L10 15 L3 15 Z"/><path d="M9 17 L25 17 L29 29 L5 29 Z"/><circle cx="17" cy="23" r="3.5" fill="#0e2f52"/></svg>
      </div>
      <div class="contact-value">555-201-0148</div>
    </div>
    <div class="contact-row">
      <div class="contact-icon">
        <svg viewBox="0 0 34 34" aria-hidden="true"><rect x="9" y="2" width="16" height="30" rx="3" fill="#fff"/><rect x="11.5" y="6" width="11" height="19" fill="#0e2f52"/><circle cx="17" cy="28.5" r="1.6" fill="#0e2f52"/></svg>
      </div>
      <div class="contact-value">555-201-0148</div>
    </div>
  </div>

  <div class="address-band">Box 274, Harlow Bend, Alberta Canada T4X 3R1</div>
</div>
</body>
</html>
```